BQ7VOLN PSD Web Designs

We need website page designs for Toren Capital, a start up HEDGE FUND MANAGEMENT business. 

Toren means 'wave' in Greek, but this is not a Greek company.

You will need to create one template that will have some common elements (such as the menu) which you will then need to apply to 6 different pages.  

The site should:
• Incorporate the Toren logo, colours and graphic elements provided with this brief.
• Have a corporate look with the provided corporate colours used in design. 
• Be professional and user-friendly 
• Have an international feel
• Be clean, clear and and easy to read
• Information to be organised in an easily accessible and logical way for time-pressed business people who are looking for efficient ways to check and manage their investment portfolios online.

We are looking for:
• Designs that do not just copy the wireframe
• Original thinking
• Extension of the brand that has already been created, throughout site.
• Design x-factor (structure, layout, readability, graphic elements)
• Corporate feel
• Judicious use of imagery (only use stock photos if they ADD meaning to your designs).

WIREFRAMES:
Attached are the wireframes of the pages that need to be designed.

Target Market(s)

Adults based in US, UK and Asia Pacific aged 25 to 70 who are corporate investors

Requirements
Must have
• Your submissions must:
• Include the logo we have attached and tie in with the business card look
• Use the menu as per the wireframes
• Include 6 PSDs (one for each of the attached wireframes)
1. Home
2. Contact Us
3. DIsclaimer
4. Our Focus
5. Privacy Policy
6. Risk Profile

```html
<!DOCTYPE html>
<html lang="en">
<head>
<meta charset="utf-8">
<title>Toren Capital – Page Designs</title>
<link href="https://fonts.googleapis.com/css2?family=PT+Sans:wght@400;700&display=swap" rel="stylesheet">
<style>
:root{
  --navy:#1b3c78;
  --bar:#1f6db0;
  --sky:#86cff2;
  --pale:#bfe5f7;
  --orange:#e8911c;
  --orange-light:#f3b049;
  --field:#fff7c2;
  --field-line:#e0d48a;
  --rule:#9fcbe6;
  --row-a:#2f6fb3;
  --row-b:#5ac6ee;
  --white:#ffffff;
}
*{box-sizing:border-box;margin:0;padding:0}
html,body{width:1200px;height:3771px;overflow:hidden}
body{position:relative;font-family:"PT Sans",Arial,sans-serif;color:var(--navy);background:#777}
.stage{position:absolute;left:0;width:1200px;background:linear-gradient(#acacac,#5a5a5a)}
.stage-1{top:0;height:1017px}
.stage-2{top:1017px;height:1303px}
.stage-3{top:2320px;height:1451px}

.page{position:absolute;left:57px;width:1095px;background:var(--white);border:2px solid var(--pale);overflow:hidden}
.page-home{top:60px;height:897px}
.page-contact{top:1077px;height:1187px}
.page-risk{top:2378px;height:1333px}
.page *{position:absolute}
.page span,.page b,.page em,.page a{position:static}

/* header */
.site-header{left:0;top:0;width:1091px;height:128px}
.swoosh{left:0;top:0}
.brand{left:10px;top:40px;display:flex;align-items:center;gap:12px;font-size:40px;font-weight:700;letter-spacing:1px;color:var(--navy);line-height:1}
.brand-dot{position:static;width:22px;height:22px;border-radius:50%;background:var(--sky)}
.nav-bar{left:0;top:91px;width:1091px;height:36px;background:var(--bar)}
.company-line{left:9px;top:11px;font-size:12px;color:var(--pale)}
.main-nav{right:30px;top:6px;display:flex;gap:40px;font-size:18px;color:var(--white)}
.main-nav span{position:static}

/* title band */
.title-band{left:0;top:126px;width:1091px;height:80px;background:var(--sky);border-bottom:2px solid var(--pale)}
.title-band h1{left:20px;top:14px;font-size:48px;font-weight:400;color:var(--white);line-height:1}

/* footer */
.footer-bar{left:0;width:1091px;height:21px;background:#9ad8f4;font-size:14px;line-height:21px;padding-left:6px;color:var(--navy)}
.footer-note{right:8px;font-size:12px;color:var(--navy)}

/* text */
.heading{font-size:20px;font-weight:700;color:var(--orange);line-height:1}
.copy{font-size:15.5px;line-height:25.5px;color:var(--navy)}
.photo{border:2px solid var(--bar)}

/* home */
.hero{left:0;top:127px;width:1091px;height:142px;background:linear-gradient(100deg,#2b4f86 0%,#5d7fae 40%,#8ea6c6 60%,#36598f 100%)}
.hero-lead{right:12px;top:12px;text-align:right;font-size:26px;font-weight:700;line-height:37px;color:var(--white)}
.hero-title{left:24px;top:96px;font-size:46px;color:var(--white);line-height:1}
.promo{left:727px;top:301px;width:334px;height:170px;background:var(--sky);padding:22px 0 0 36px;font-size:22px;font-weight:700;line-height:40px;color:var(--navy)}
.promo div{position:static}
.promo .big{font-size:32px}

/* sidebar */
.sidebar-rule{width:2px;background:var(--pale)}
.side-link{font-size:15px;font-weight:700;color:var(--navy)}
.side-title{font-size:20px;font-weight:700;color:var(--orange)}
.side-line{height:1px;background:var(--rule)}

/* form */
.label{font-size:15px;color:var(--navy);white-space:nowrap}
.label-right{text-align:right}
.field{height:24px;background:var(--field);border:1px solid var(--field-line)}
.hint{font-size:10px;color:var(--navy)}
.form-rule{height:1px;background:var(--rule)}
.radio{display:flex;align-items:center;gap:8px;font-size:15px;color:var(--navy)}
.radio i{position:static;display:block;width:14px;height:14px;border:1.5px solid var(--bar);border-radius:50%;background:var(--white)}
.submit{width:199px;height:34px;border:1px solid #888;background:linear-gradient(#f4f4f4,#cfcfcf);font-size:16px;text-align:center;line-height:32px;color:#222}

/* risk tables */
.risk-table{left:560px;width:286px}
.risk-table .t-head{position:relative;height:34px;background:linear-gradient(90deg,var(--orange),var(--orange-light));color:var(--white);font-weight:700;font-size:18px;line-height:34px;padding-left:7px}
.risk-table .t-cols,.risk-table .t-row{position:relative;display:grid;align-items:center;padding:0 6px;color:var(--white);font-size:17px;border-top:1px solid var(--white)}
.risk-table .t-cols{height:31px;background:var(--row-a);font-weight:700}
.risk-table .t-row{height:30px;background:linear-gradient(90deg,var(--row-a),var(--row-b))}
.risk-table .t-row:nth-child(odd){background:linear-gradient(90deg,#3d86c8,#7ad4f3)}
.risk-table span{text-align:right}
.risk-table span:first-child{text-align:left}
.two-col{grid-template-columns:1fr 70px}
.three-col{grid-template-columns:1fr 70px 80px}
.pos-col{grid-template-columns:1fr 70px 70px}
.t-head.pos-head{display:grid;grid-template-columns:1fr 58px 82px;padding-right:6px}
.t-head.pos-head span{text-align:right;position:static}
.t-head.pos-head .small{font-size:11px;line-height:12px;text-align:center;align-self:center}
.chart-text{font-family:"PT Sans",Arial,sans-serif;fill:var(--navy)}
</style>
</head>
<body>

<div class="stage stage-1"></div>
<div class="stage stage-2"></div>
<div class="stage stage-3"></div>

<!-- HOME -->
<section class="page page-home">
  <header class="site-header">
    <svg class="swoosh" width="1091" height="91" viewBox="0 0 1091 91">
      <path d="M300 91 C650 84 930 55 1091 0 L1091 91 Z" fill="#c6e9f8"/>
      <path d="M560 91 C820 84 990 60 1091 28 L1091 91 Z" fill="#7fcdf0"/>
    </svg>
    <div class="brand"><span class="brand-dot"></span>TOREN CAPITAL</div>
    <nav class="nav-bar">
      <div class="company-line">TOREN CAPITAL Pty Ltd</div>
      <div class="main-nav"><span>Our Focus</span><span>Contact Us</span></div>
    </nav>
  </header>

  <div class="hero" role="img" aria-label="Photo of glass office towers in blue tones">
    <div class="hero-lead">Lorem ipsum dolor sit amet, consectetur adipiscing elit.<br>Nullam fringilla lobortis velit at porttitor.</div>
    <div class="hero-title">Welcome</div>
  </div>

  <h2 class="heading" style="left:31px;top:293px">Lorem ipsum dolor sit amet</h2>
  <p class="copy" style="left:31px;top:316px;width:615px">Consectetur adipiscing elit. Nullam fringilla lobortis velit at porttitor. Duis iaculis felis et nisi facilisis at ultricies diam pellentesque. Nunc id nibh metus. Quisque at est vestibulum ante pulvinar hendrerit eget in sapien. Nunc vel lobortis erat. Nunc non sem mi. Sed auctor dolor sit amet quam porta ut congue elit imperdiet. Praesent sed justo nisl, in pulvinar massa. Etiam et nisl ligula, consectetur pulvinar leo. Quisque nisi nulla, pulvinar non vehicula ac, pellentesque sit amet justo.</p>

  <div class="promo">
    <div>Lorem ipsum <span class="big">dolor</span></div>
    <div>sit <span class="big">amet</span>, consectetur</div>
    <div>adipiscing elit &nbsp;<span class="big">&gt;&gt;</span></div>
  </div>

  <div class="photo" style="left:38px;top:509px;width:386px;height:287px;background:linear-gradient(135deg,#e6edf3,#b7c6d6 55%,#2f4fa8 80%,#dfe6ee)" role="img" aria-label="Photo of a calculator, pen and stock chart printout"></div>

  <h2 class="heading" style="left:457px;top:502px">Suspendisse lobortis dapibus augue</h2>
  <p class="copy" style="left:457px;top:525px;width:615px">id pellentesque arcu tincidunt quis. Aenean blandit blandit placerat. Curabitur blandit, ligula eu mattis condimentum, dolorrisus rhoncus massa, in viverra justo felis mollis diam. Nulla in magna id turpis ornare tincidunt. Ut augue metus, congue ut luctus vel, semper ac tortor. Quisqueauctor enim id nisi pretium mattis molestie vel orci. Proin nisl nisi, vestibulum eu malesuada id, semper ut felis. Phasellus eu ligula non velit mattis posuere.</p>
  <p class="copy" style="left:457px;top:703px;width:615px">Suspendisse id sem leo, nec molestie leo. Vestibulum dui diam, lacinia eget cursus in, interdum eu eros. Curabitur dictum, orci et varius adipiscing, odio nunc condimentum nibh, a lacinia enim urna eu lacus. Pellentesque dapibus nisl lectus. Nunc in erat risus, lobortis viverra lorem. Sed at aliquet sapien.</p>

  <footer>
    <div class="footer-bar" style="top:845px">Privacy Policy &nbsp;| &nbsp;Disclaimer</div>
    <div class="footer-note" style="top:874px">Toren Captital Pty Ltd</div>
  </footer>
</section>

<!-- CONTACT -->
<section class="page page-contact">
  <header class="site-header">
    <svg class="swoosh" width="1091" height="91" viewBox="0 0 1091 91">
      <path d="M300 91 C650 84 930 55 1091 0 L1091 91 Z" fill="#c6e9f8"/>
      <path d="M560 91 C820 84 990 60 1091 28 L1091 91 Z" fill="#7fcdf0"/>
    </svg>
    <div class="brand"><span class="brand-dot"></span>TOREN CAPITAL</div>
    <nav class="nav-bar">
      <div class="company-line">TOREN CAPITAL Pty Ltd</div>
      <div class="main-nav"><span>Our Focus</span><span>Contact Us</span></div>
    </nav>
  </header>
  <div class="title-band"><h1>Contact Us</h1></div>

  <div class="sidebar-rule" style="left:869px;top:206px;height:920px"></div>
  <div class="side-link" style="left:884px;top:235px">Our Focus</div>
  <div class="side-link" style="left:884px;top:260px">Contact Us</div>
  <div class="side-line" style="left:876px;top:291px;width:198px"></div>
  <div class="side-title" style="left:879px;top:301px">Quick Links</div>
  <div class="side-link" style="left:884px;top:333px">Toren Home</div>
  <div class="side-link" style="left:884px;top:358px">Contact Us</div>

  <div class="heading" style="left:32px;top:230px;font-size:16px">By Phone/Mail</div>
  <div class="label" style="left:32px;top:280px;font-weight:700">TOREN Capital Pty Ltd</div>
  <div class="label" style="left:32px;top:305px;line-height:25.5px">12/40 Harbour Lane<br>Melbourne Vic 3000<br>Australia</div>
  <div class="label label-right" style="right:535px;top:305px;line-height:25.5px">Phone: 03 9555 0142<br>Fax: 03 9555 0143<br>Email: <span style="color:#1f6fd0">info@torencapital.example</span></div>

  <div class="heading" style="left:32px;top:452px;font-size:19px">Or Email</div>
  <div class="form-rule" style="left:12px;top:480px;width:854px"></div>
  <div class="heading" style="left:34px;top:493px;font-size:19px">Your Details</div>

  <div class="label label-right" style="right:944px;top:531px">First Name:</div>
  <div class="field" style="left:164px;top:529px;width:430px"></div>
  <div class="label label-right" style="right:944px;top:565px">Last Name:</div>
  <div class="field" style="left:164px;top:563px;width:430px"></div>

  <div class="label" style="left:38px;top:599px;font-weight:700">Contact Phone</div>
  <div class="label label-right" style="right:944px;top:634px">Country Code:</div>
  <div class="field" style="left:164px;top:632px;width:83px"></div>
  <div class="label" style="left:274px;top:634px">Area Code:</div>
  <div class="field" style="left:364px;top:632px;width:84px"></div>
  <div class="label" style="left:465px;top:634px">Ph No:</div>
  <div class="field" style="left:525px;top:632px;width:166px"></div>
  <div class="hint" style="left:164px;top:659px">Please enter the preferred number you would like us to contact you at</div>

  <div class="label label-right" style="right:944px;top:695px">Email Address:</div>
  <div class="field" style="left:164px;top:693px;width:430px"></div>
  <div class="hint" style="left:164px;top:722px">Please enter the preferred email you would like us to contact you at</div>

  <div class="label" style="left:161px;top:764px">Preferred contact method:</div>
  <div class="radio" style="left:365px;top:764px"><i></i>Email</div>
  <div class="radio" style="left:477px;top:764px"><i></i>Phone</div>

  <div class="form-rule" style="left:12px;top:820px;width:854px"></div>
  <div class="heading" style="left:34px;top:833px;font-size:19px">Your Enquiry</div>
  <div class="label" style="left:132px;top:874px">Select Enquiry Category:</div>
  <div class="radio" style="left:348px;top:874px"><i></i>Investor Enquiries</div>
  <div class="radio" style="left:523px;top:874px"><i></i>Career Enquiries</div>
  <div class="radio" style="left:692px;top:874px"><i></i>Other Enquiries</div>

  <div class="label" style="left:35px;top:921px">Further Description (Tell us more...):</div>
  <div class="field" style="left:37px;top:948px;width:829px;height:104px"></div>
  <div class="submit" style="left:285px;top:1074px">Submit</div>

  <footer>
    <div class="footer-bar" style="top:1128px">Privacy Policy &nbsp;| &nbsp;Disclaimer</div>
    <div class="footer-note" style="top:1158px">Toren Captital Pty Ltd</div>
  </footer>
</section>

<!-- RISK -->
<section class="page page-risk">
  <header class="site-header">
    <svg class="swoosh" width="1091" height="91" viewBox="0 0 1091 91">
      <path d="M300 91 C650 84 930 55 1091 0 L1091 91 Z" fill="#c6e9f8"/>
      <path d="M560 91 C820 84 990 60 1091 28 L1091 91 Z" fill="#7fcdf0"/>
    </svg>
    <div class="brand"><span class="brand-dot"></span>TOREN CAPITAL</div>
    <nav class="nav-bar">
      <div class="company-line">TOREN CAPITAL Pty Ltd</div>
      <div class="main-nav"><span>Our Focus</span><span>Contact Us</span></div>
    </nav>
  </header>
  <div class="title-band" style="top:124px"><h1>Risk Management</h1></div>

  <div style="left:1px;top:206px;width:290px;height:87px;background:linear-gradient(120deg,#d9cbb6,#b39a7d 50%,#eae2d6)" role="img" aria-label="Photo of a magnifying glass over an annual market report"></div>
  <div style="left:291px;top:206px;width:290px;height:87px;background:linear-gradient(120deg,#1f3f78,#3f6aa6 50%,#223f72)" role="img" aria-label="Photo of a stock price board"></div>
  <div style="left:581px;top:206px;width:288px;height:87px;background:linear-gradient(120deg,#f1f3f6,#c9ced6 60%,#7c8596)" role="img" aria-label="Photo of a business presentation"></div>

  <div class="sidebar-rule" style="left:871px;top:206px;height:1073px"></div>
  <div class="side-link" style="left:890px;top:215px">Investor Lounge</div>
  <div class="side-link" style="left:919px;top:238px">Risk Management</div>
  <div class="side-link" style="left:919px;top:263px">Newsletter</div>
  <div class="side-line" style="left:876px;top:293px;width:198px"></div>
  <div class="side-title" style="left:883px;top:304px">Quick Links</div>
  <div class="side-link" style="left:890px;top:335px">Toren Home</div>
  <div class="side-link" style="left:890px;top:361px">Contact Us</div>

  <h2 class="heading" style="left:19px;top:304px">Lorem ipsum dolor sit amet</h2>
  <p class="copy" style="left:19px;top:327px;width:830px">Consectetur adipiscing elit. Nullam fringilla lobortis velit at porttitor. Duis iaculis felis et nisi facilisis at ultricies diam pellentesque. Nunc id nibh metus. Quisque at est vestibulum ante pulvinar hendrerit eget in sapien. Nunc vel lobortis erat. Nunc non sem mi. Sed auctor dolor sit amet quam porta ut congue elit imperdiet. Praesent sed justo nisl, in pulvinar massa. Etiam et nisl ligula, consectetur pulvinar leo. Quisque nisi nulla, pulvinar non vehicula ac, pellentesque sit amet justo.</p>

  <svg style="left:0;top:480px" width="560" height="740" viewBox="0 0 560 740" class="charts">
    <defs>
      <linearGradient id="gOrange" x1="0" y1="0" x2="1" y2="1"><stop offset="0" stop-color="#f4b85a"/><stop offset="1" stop-color="#e08a12"/></linearGradient>
      <linearGradient id="gBlue" x1="0" y1="0" x2="1" y2="1"><stop offset="0" stop-color="#6aa6d8"/><stop offset="1" stop-color="#2f6cb0"/></linearGradient>
      <linearGradient id="gLight" x1="0" y1="0" x2="1" y2="1"><stop offset="0" stop-color="#d4effb"/><stop offset="1" stop-color="#8fd3f3"/></linearGradient>
      <g id="pie">
        <circle r="84" fill="#eef3f7"/>
        <path d="M0 0 L0 -80 A80 80 0 0 1 80 0 Z" fill="url(#gBlue)"/>
        <path d="M0 0 L80 0 A80 80 0 0 1 40 69.3 Z" fill="url(#gLight)"/>
        <path d="M0 0 L40 69.3 A80 80 0 1 1 0 -80 Z" fill="url(#gOrange)"/>
        <path d="M-60 -60 L-30 -25 M45 -25 L80 -60 M45 40 L82 70" stroke="#222" stroke-width="1" fill="none"/>
        <text x="-96" y="-73" font-size="15" text-anchor="middle" class="chart-text">Special Sits</text>
        <text x="-96" y="-53" font-size="15" text-anchor="middle" class="chart-text">70%</text>
        <text x="109" y="-77" font-size="15" text-anchor="middle" class="chart-text">ARB</text>
        <text x="109" y="-57" font-size="15" text-anchor="middle" class="chart-text">20%</text>
        <text x="109" y="63" font-size="15" text-anchor="middle" class="chart-text">IPO</text>
        <text x="109" y="83" font-size="15" text-anchor="middle" class="chart-text">20%</text>
      </g>
    </defs>

    <!-- gross exposure -->
    <text x="155" y="40" font-size="16" font-weight="700" text-anchor="middle" class="chart-text">Gross Exposure</text>
    <rect x="78" y="94" width="165" height="57" fill="url(#gOrange)"/>
    <rect x="78" y="151" width="165" height="83" fill="url(#gBlue)"/>
    <text x="160" y="128" font-size="15" text-anchor="middle" class="chart-text">Maximum</text>
    <text x="160" y="197" font-size="15" text-anchor="middle" class="chart-text">Actual</text>
    <g stroke="#333" stroke-width="1">
      <line x1="75" y1="66" x2="75" y2="246"/><line x1="75" y1="236" x2="250" y2="236"/>
      <line x1="70" y1="70" x2="80" y2="70"/><line x1="70" y1="91" x2="80" y2="91"/><line x1="70" y1="112" x2="80" y2="112"/><line x1="70" y1="132" x2="80" y2="132"/><line x1="70" y1="153" x2="80" y2="153"/><line x1="70" y1="174" x2="80" y2="174"/><line x1="70" y1="195" x2="80" y2="195"/><line x1="70" y1="215" x2="80" y2="215"/>
    </g>
    <g font-size="14" text-anchor="end" class="chart-text">
      <text x="66" y="75">160</text><text x="66" y="96">140</text><text x="66" y="117">120</text><text x="66" y="137">100</text><text x="66" y="158">80</text><text x="66" y="179">60</text><text x="66" y="200">40</text><text x="66" y="220">20</text><text x="66" y="241">0</text>
    </g>
    <text x="18" y="158" font-size="14" class="chart-text">%</text>

    <!-- net exposure -->
    <text x="150" y="330" font-size="16" font-weight="700" text-anchor="middle" class="chart-text">Net Exposure</text>
    <rect x="78" y="357" width="165" height="40" fill="url(#gOrange)"/>
    <rect x="78" y="397" width="165" height="41" fill="url(#gBlue)"/>
    <rect x="78" y="438" width="165" height="58" fill="url(#gLight)"/>
    <text x="160" y="382" font-size="15" text-anchor="middle" class="chart-text">Max Long</text>
    <text x="160" y="422" font-size="15" text-anchor="middle" class="chart-text">Actual</text>
    <text x="160" y="472" font-size="15" text-anchor="middle" class="chart-text">Max Short</text>
    <g stroke="#333" stroke-width="1">
      <line x1="75" y1="355" x2="75" y2="510"/>
      <line x1="70" y1="373" x2="80" y2="373"/><line x1="70" y1="394" x2="80" y2="394"/><line x1="70" y1="415" x2="80" y2="415"/><line x1="70" y1="436" x2="80" y2="436"/><line x1="70" y1="456" x2="80" y2="456"/><line x1="70" y1="477" x2="80" y2="477"/><line x1="70" y1="498" x2="80" y2="498"/>
    </g>
    <g font-size="14" text-anchor="end" class="chart-text">
      <text x="66" y="378">60</text><text x="66" y="399">40</text><text x="66" y="420">20</text><text x="66" y="441">0</text><text x="66" y="461">-20</text><text x="66" y="482">-40</text><text x="66" y="503">-60</text>
    </g>
    <text x="18" y="441" font-size="14" class="chart-text">%</text>

    <!-- pies -->
    <text x="460" y="23" font-size="16" font-weight="700" text-anchor="middle" class="chart-text">Strategy Allocation</text>
    <use href="#pie" x="405" y="129"/>
    <text x="458" y="268" font-size="16" font-weight="700" text-anchor="middle" class="chart-text">Country Allocation</text>
    <use href="#pie" x="405" y="376"/>
    <text x="460" y="517" font-size="16" font-weight="700" text-anchor="middle" class="chart-text">Sector Allocation</text>
    <use href="#pie" x="405" y="625"/>
  </svg>

  <div class="risk-table" style="top:465px">
    <div class="t-head">Historical Risk Parameters</div>
    <div class="t-row two-col"><span>Sandard Deveiation</span><span>6.22</span></div>
    <div class="t-row two-col"><span>Sortino</span><span>1.92</span></div>
    <div class="t-row two-col"><span>Sharpe</span><span>1.02</span></div>
  </div>

  <div class="risk-table" style="top:607px">
    <div class="t-head">Live Portfolio Risk</div>
    <div class="t-cols three-col"><span>Parameter</span><span>Max</span><span>Current</span></div>
    <div class="t-row three-col"><span>Single Name</span><span>8</span><span>7</span></div>
    <div class="t-row three-col"><span>Sector</span><span>25</span><span>20</span></div>
    <div class="t-row three-col"><span>Country</span><span>50</span><span>30</span></div>
    <div class="t-row three-col"><span>Gross</span><span>150</span><span>90</span></div>
    <div class="t-row three-col"><span>Net</span><span>+/- 50</span><span>30</span></div>
    <div class="t-row three-col"><span>Var</span><span>?</span><span>?</span></div>
  </div>

  <div class="risk-table" style="top:871px">
    <div class="t-head">Estimated MTD return</div>
    <div class="t-cols two-col"><span>Signal Contribution</span><span>%</span></div>
    <div class="t-row two-col"><span>IPO</span><span>0.5</span></div>
    <div class="t-row two-col"><span>ARB</span><span>0.35</span></div>
    <div class="t-row two-col"><span>S/SITS</span><span>1.2</span></div>
    <div class="t-row two-col"><span>TOTAL</span><span>2.05</span></div>
  </div>

  <div class="risk-table" style="top:1073px">
    <div class="t-head pos-head"><span style="text-align:left">Top 5 Positions</span><span class="small">Long/<br>Short</span><span>% AUM</span></div>
    <div class="t-row pos-col"><span>Harlow Mining</span><span>Long</span><span>7%</span></div>
    <div class="t-row pos-col"><span>Eastline Telecom</span><span>Long</span><span>6%</span></div>
    <div class="t-row pos-col"><span>Crestfield Resources</span><span>Short</span><span>6%</span></div>
    <div class="t-row pos-col"><span>Meridian Tech</span><span>Short</span><span>5%</span></div>
    <div class="t-row pos-col"><span>Aoki Securities</span><span>Long</span><span>5%</span></div>
  </div>

  <footer>
    <div class="footer-bar" style="top:1279px">Privacy Policy &nbsp;| &nbsp;Disclaimer</div>
    <div class="footer-note" style="top:1309px">Toren Captital Pty Ltd</div>
  </footer>
</section>

</body>
</html>
```